BROVA Website Redesign - More modern look & feel

I will upload high resolution copies of the BROVA logo tomorrow
Please make website responsive/mobile friendly
Use simple and clean black & white, easy to read text, color transitions & translucent, shadows, reflections/metallic
Alternate between white and black backgrounds from section to section but start with white background at top of fold/hero section
Freeze top bar & change to dark when scrolling down
If possible, have site convert to black background when consumer using dark mode on their phone or browser
Use high quality images of various types of business payments, in-store and online
Make sure photos are inclusive of race & sex/gender and show payments & business interaction
Use a high quality image of a website payment checkout screen
Use clear banner for logos under hero section
CTA at each section (bold caps with bright green)
Use only one shade of green
Use consistent font/text
Use Brova building image at bottom in get started section
US businesses
Fintech (financial technology) / merchant services
1 page

```html
<!DOCTYPE html>
<html lang="en">
<head>
<meta charset="utf-8">
<title>Brova — Website Screens</title>
<link rel="stylesheet" href="https://fonts.googleapis.com/css2?family=Inter:wght@400;500;600;700&display=swap">
<style>
:root{
  --board:#e6e6e6;
  --ink:#1b1d1d;
  --ink-2:#222625;
  --deep:#1f4a40;
  --deep-2:#2a5d52;
  --mint:#22edc1;
  --paper:#eef2f1;
  --paper-2:#f6f7f7;
  --muted:#8c9895;
  --line-dark:rgba(255,255,255,.14);
  --line-light:rgba(0,0,0,.14);
}
*{box-sizing:border-box;margin:0;padding:0}
html,body{width:1200px;height:602px;overflow:hidden;background:var(--board)}
body{font-family:"Inter",Arial,sans-serif}
.board{position:relative;width:2576px;height:1293px;transform:scale(.46584);transform-origin:0 0}
.screen{position:absolute;width:458px;height:257px;overflow:hidden;color:#fff}
.screen--short{height:173px}
.dark{background:linear-gradient(160deg,var(--ink) 35%,var(--ink-2) 55%,var(--deep) 130%)}
.dark-teal{background:linear-gradient(150deg,#1c2321 0%,var(--deep) 100%)}
.light{background:linear-gradient(160deg,var(--paper-2) 40%,#e4f1ee 100%);color:var(--ink)}
.mint{background:var(--mint);color:var(--ink)}

/* nav */
.nav{position:absolute;top:10px;left:20px;right:20px;height:8px;display:flex;align-items:center;font-size:3.2px;color:rgba(255,255,255,.45)}
.light .nav,.mint .nav{color:rgba(0,0,0,.45)}
.nav-links{display:flex;gap:9px}
.nav-links span:first-child{color:inherit;opacity:1;border-bottom:.6px solid var(--mint)}
.brand{position:absolute;left:50%;transform:translateX(-50%);font-size:5px;letter-spacing:4px;color:#fff}
.light .brand,.mint .brand{color:var(--ink)}
.login{margin-left:auto;background:var(--mint);color:var(--ink);border-radius:2px;padding:1.5px 4px;font-size:3px;font-weight:600}
.mint .login{background:var(--ink);color:var(--mint)}

.side-dots{position:absolute;right:20px;bottom:20px;display:flex;flex-direction:column;gap:5px}
.side-dots i{display:block;width:1.5px;height:1.5px;border-radius:50%;background:currentColor;opacity:.5}
.side-dots i:first-child{opacity:1}

/* type */
.hero-title{position:absolute;left:20px;top:44px;font-size:50px;font-weight:500;line-height:46px;letter-spacing:-.5px}
.chips{position:absolute;left:22px;display:flex;gap:6px}
.chip{display:flex;align-items:center;gap:3px;border:.6px solid var(--line-dark);border-radius:3px;padding:4px 6px;font-size:4.4px;background:rgba(255,255,255,.03)}
.light .chip,.mint .chip{border-color:var(--line-light)}
.chip i{width:2px;height:2px;border-radius:50%;background:var(--mint);opacity:.7}
.mint .chip i{background:var(--ink)}
.chip b{color:var(--mint);font-weight:500}
.mint .chip b{color:var(--ink)}
.cta-row{position:absolute;left:28px;bottom:20px;display:flex;align-items:center;gap:12px;font-size:4.4px}
.btn{display:inline-block;border:.7px solid var(--mint);border-radius:8px;padding:3px 9px;font-size:3.4px;color:#fff}
.light .btn{border-color:rgba(0,0,0,.35);color:var(--ink)}
.mint .btn{border-color:var(--ink);color:var(--ink)}
.art{position:absolute}

.section-title{position:absolute;font-weight:400}
.features{position:absolute;display:flex;flex-direction:column;gap:9px;font-size:3.2px;color:rgba(255,255,255,.5);width:90px}
.light .features{color:rgba(0,0,0,.45)}
.features h4{font-size:4.2px;font-weight:500;color:#fff;margin-bottom:1.5px}
.light .features h4{color:var(--ink)}
.features.cols{flex-direction:row;flex-wrap:wrap;gap:10px 18px;width:190px}
.features.cols div{width:86px}
.green{color:var(--mint)}
.rule{position:absolute;height:.7px;background:var(--line-dark)}
.light .rule{background:var(--line-light)}
.phone{position:absolute;border-radius:16px;background:linear-gradient(160deg,#3b3f3f,#0f1111 40%,#1a3c35);border:2px solid #5b615f}
.caps{font-weight:500;letter-spacing:.5px}
.para{position:absolute;font-size:3px;line-height:4px;color:rgba(255,255,255,.5);width:100px}
.light .para{color:rgba(0,0,0,.5)}
.arrow-dot{position:absolute;width:16px;height:16px;border-radius:50%;background:#1e4b41;display:flex;align-items:center;justify-content:center}
.badge{position:absolute;display:flex;align-items:center;gap:5px;font-size:3.6px;line-height:4.4px;background:rgba(255,255,255,.05);border-radius:3px;padding:5px 8px}
</style>
</head>
<body>
<main class="board">

<!-- ROW 1 -->
<section class="screen dark" style="left:80px;top:77px">
  <nav class="nav"><div class="nav-links"><span>Home</span><span>Industries</span><span>Solutions</span><span>Blog</span><span>Contact</span></div><div class="brand">BROVA</div><span class="login">Log in</span></nav>
  <h1 class="hero-title">Payments<br>Simplified</h1>
  <div class="art" role="img" aria-label="Mint wireframe of two twisted funnel shapes" style="left:260px;top:34px;width:180px;height:186px;border-radius:50%;background:radial-gradient(circle,rgba(34,237,193,.22),transparent 70%)"></div>
  <div class="chips" style="top:157px"><span class="chip"><i></i>Quick &amp; Easy setup for all types of businesses</span></div>
  <div class="chips" style="top:183px"><span class="chip"><i></i>Transparent pricing</span><span class="chip"><i></i>Accept payments <b>your way</b></span></div>
  <div class="cta-row"><span class="btn">Get Started</span><span>Free to Get Started!</span></div>
  <div class="side-dots"><i></i><i></i><i></i><i></i></div>
</section>

<section class="screen dark" style="left:572px;top:77px">
  <nav class="nav"><div class="nav-links"><span>Home</span><span>Industries</span><span>Solutions</span><span>Blog</span><span>Contact</span></div><div class="brand">BROVA</div><span class="login">Log in</span></nav>
  <h1 class="hero-title" style="top:50px;font-size:46px;line-height:42px">Payments<br>Simplified</h1>
  <div class="art" role="img" aria-label="Large mint abstract brand-colour graphic" style="left:230px;top:40px;width:200px;height:217px;background:linear-gradient(170deg,rgba(34,237,193,.55),rgba(34,237,193,.15))"></div>
  <div class="chips" style="top:148px"><span class="chip"><i></i>Quick &amp; Easy setup for all types of businesses</span></div>
  <div class="chips" style="top:176px"><span class="chip"><i></i>Transparent pricing</span><span class="chip"><i></i>Accept payments <b>your way</b></span></div>
  <div class="cta-row"><span class="btn">Get Started</span><span>Free to Get Started!</span></div>
  <div class="side-dots"><i></i><i></i><i></i><i></i></div>
</section>

<section class="screen mint" style="left:1065px;top:77px">
  <nav class="nav"><div class="nav-links"><span>Home</span><span>Industries</span><span>Solutions</span><span>Blog</span><span>Contact</span></div><div class="brand">BROVA</div><span class="login">Log in</span></nav>
  <h1 class="hero-title">Payments<br>Simplified</h1>
  <div class="art" role="img" aria-label="Black line wireframe of two twisted funnel shapes" style="left:260px;top:34px;width:180px;height:186px;border-radius:50%;background:radial-gradient(circle,rgba(0,0,0,.1),transparent 70%)"></div>
  <div class="chips" style="top:157px"><span class="chip"><i></i>Quick &amp; Easy setup for all types of businesses</span></div>
  <div class="chips" style="top:183px"><span class="chip"><i></i>Transparent pricing</span><span class="chip"><i></i>Accept payments <b>your way</b></span></div>
  <div class="cta-row"><span class="btn">Get Started</span><span>Free to Get Started!</span></div>
  <div class="side-dots"><i></i><i></i><i></i><i></i></div>
</section>

<section class="screen dark" style="left:1558px;top:77px">
  <svg class="art" width="458" height="257" viewBox="0 0 458 257" style="left:0;top:0">
    <polygon points="290,0 330,0 390,257 350,257" fill="#24574c" opacity=".9"/>
    <polygon points="210,257 458,60 458,110 270,257" fill="#24574c" opacity=".8"/>
  </svg>
  <nav class="nav"><div class="nav-links"><span>Home</span><span>Industries</span><span>Solutions</span><span>Blog</span><span>Contact</span></div><div class="brand">BROVA</div><span class="login">Log in</span></nav>
  <h1 class="hero-title">Payments<br>Simplified</h1>
  <div class="chips" style="top:148px"><span class="chip"><i></i>Quick &amp; Easy setup for all types of businesses</span></div>
  <div class="chips" style="top:176px"><span class="chip"><i></i>Transparent pricing</span><span class="chip"><i></i>Accept payments <b>your way</b></span></div>
  <div class="cta-row"><span class="btn">Get Started</span><span>Free to Get Started!</span></div>
  <div class="side-dots"><i></i><i></i><i></i><i></i></div>
</section>

<section class="screen dark" style="left:2051px;top:77px">
  <div class="art" role="img" aria-label="Grainy teal sphere with dark speckled edge" style="left:230px;top:30px;width:210px;height:210px;border-radius:50%;background:radial-gradient(circle at 55% 40%,#4a8c7e,#2f6458 50%,rgba(30,40,38,.2) 75%)"></div>
  <nav class="nav"><div class="nav-links"><span>Home</span><span>Industries</span><span>Solutions</span><span>Blog</span><span>Contact</span></div><div class="brand">BROVA</div><span class="login">Log in</span></nav>
  <h1 class="hero-title">Payments<br>Simplified</h1>
  <div class="chips" style="top:148px"><span class="chip"><i></i>Quick &amp; Easy setup for all types of businesses</span></div>
  <div class="chips" style="top:176px"><span class="chip"><i></i>Transparent pricing</span><span class="chip"><i></i>Accept payments <b>your way</b></span></div>
  <div class="cta-row"><span class="btn">Get Started</span><span>Free to Get Started!</span></div>
  <div class="side-dots"><i></i><i></i><i></i><i></i></div>
</section>

<!-- ROW 2 -->
<section class="screen dark" style="left:80px;top:370px">
  <nav class="nav"><div class="nav-links"><span>Home</span><span>Industries</span><span>Solutions</span><span>Blog</span><span>Contact</span></div><div class="brand">BROVA</div><span class="login">Log in</span></nav>
  <div class="art" role="img" aria-label="Fan of mint lines converging to a point" style="left:160px;top:14px;width:130px;height:230px;background:linear-gradient(90deg,rgba(34,237,193,.05),rgba(34,237,193,.35));clip-path:polygon(0 0,100% 50%,0 100%)"></div>
  <h2 class="section-title" style="left:19px;top:95px;font-size:22px">Subscription</h2>
  <div class="rule" style="left:19px;top:124px;width:150px"></div>
  <div class="features" style="left:306px;top:74px">
    <div><h4>Free Quote</h4>We will beat your current rate.</div>
    <div><h4>Create reusable CSS classes</h4>Work with a class system to make style changes across many elements.</div>
    <div><h4>Pass your fees to your customers</h4>Brova offers convenience fees and cash discount.</div>
    <div><h4>Fine-tune typography</h4>Use any font, adjust from tracking to line height.</div>
  </div>
  <span class="btn" style="position:absolute;left:303px;top:218px">Learn More</span>
  <div class="side-dots"><i></i><i></i><i></i></div>
</section>

<section class="screen light" style="left:572px;top:370px">
  <nav class="nav"><div class="nav-links"><span>Home</span><span>Industries</span><span>Solutions</span><span>Blog</span><span>Contact</span></div><div class="brand">BROVA</div><span class="login">Log in</span></nav>
  <div class="art" role="img" aria-label="Fan of grey lines converging to a point" style="left:160px;top:14px;width:130px;height:230px;background:linear-gradient(90deg,rgba(0,0,0,.03),rgba(0,0,0,.2));clip-path:polygon(0 0,100% 50%,0 100%)"></div>
  <h2 class="section-title" style="left:19px;top:95px;font-size:22px">Subscription</h2>
  <div class="rule" style="left:19px;top:124px;width:150px"></div>
  <div class="features" style="left:306px;top:74px">
    <div><h4>Free Quote</h4>We will beat your current rate.</div>
    <div><h4>Create reusable CSS classes</h4>Work with a class system to make style changes across many elements.</div>
    <div><h4>Pass your fees to your customers</h4>Brova offers convenience fees and cash discount.</div>
    <div><h4>Fine-tune typography</h4>Use any font, adjust from tracking to line height.</div>
  </div>
  <span class="btn" style="position:absolute;left:303px;top:218px">Learn More</span>
  <div class="side-dots"><i></i><i></i><i></i></div>
</section>

<section class="screen light" style="left:1065px;top:370px">
  <nav class="nav"><div class="nav-links"><span>Home</span><span>Industries</span><span>Solutions</span><span>Blog</span><span>Contact</span></div><div class="brand">BROVA</div><span class="login">Log in</span></nav>
  <div style="position:absolute;left:18px;top:28px;width:207px;height:210px;background:rgba(255,255,255,.6);border-radius:4px;text-align:center">
    <h2 style="margin-top:12px;font-size:26px;font-weight:400">Subscription</h2>
    <p style="font-size:10px;margin-top:2px">Pay interchange costs +</p>
    <p style="font-size:3.4px;color:var(--muted);margin-top:2px">low monthly fee starting at $99</p>
    <div role="img" aria-label="Wireframe funnel graphic" style="margin:12px auto 0;width:140px;height:70px;border-radius:50%;background:radial-gradient(ellipse,rgba(0,0,0,.12),transparent 70%)"></div>
    <span class="btn" style="margin-top:12px">Get Started</span>
  </div>
  <div style="position:absolute;left:233px;top:28px;width:207px;height:175px;background:rgba(230,238,236,.8);border-radius:4px"></div>
  <div class="phone" role="img" aria-label="Smartphone showing the app screen" style="left:248px;top:44px;width:92px;height:194px"></div>
  <div class="features" style="left:354px;top:54px;width:70px;gap:8px">
    <div><h4>Free Quote</h4>We will beat your current rate.</div>
    <div><h4>Pass your fees to your customers</h4>Convenience fees and cash discount.</div>
    <div><h4>Create reusable CSS classes</h4>Change styles across many elements.</div>
    <div><h4>Fine-tune typography</h4>Adjust tracking to line height.</div>
  </div>
  <div class="side-dots"><i></i><i></i><i></i></div>
</section>

<section class="screen dark" style="left:1558px;top:370px">
  <nav class="nav"><div class="nav-links"><span>Home</span><span>Industries</span><span>Solutions</span><span>Blog</span><span>Contact</span></div><div class="brand">BROVA</div><span class="login">Log in</span></nav>
  <div class="phone" role="img" aria-label="Smartphone showing the app screen" style="left:55px;top:46px;width:132px;height:230px;border-radius:20px"></div>
  <h2 class="section-title" style="left:224px;top:54px;font-size:26px">Subscription</h2>
  <p style="position:absolute;left:224px;top:90px;font-size:10px" class="green">Pay interchange costs +</p>
  <p style="position:absolute;left:224px;top:108px;font-size:3.4px;color:var(--muted)">low monthly fee starting at $99</p>
  <div class="features cols" style="left:224px;top:134px">
    <div><h4>Free Quote</h4>We will beat your current rate.</div>
    <div><h4>Pass your fees to your customers</h4>Convenience fees and cash discount.</div>
    <div><h4>Create reusable CSS classes</h4>Change styles across many elements.</div>
    <div><h4>Fine-tune typography</h4>Adjust from tracking to line height.</div>
  </div>
  <span class="btn" style="position:absolute;left:220px;top:218px">Get Started</span>
  <div class="side-dots"><i></i><i></i><i></i></div>
</section>

<section class="screen dark-teal" style="left:2051px;top:370px">
  <nav class="nav"><div class="nav-links"><span>Home</span><span>Industries</span><span>Solutions</span><span>Blog</span><span>Contact</span></div><div class="brand">BROVA</div><span class="login">Log in</span></nav>
  <h2 class="section-title green" style="left:20px;top:50px;font-size:40px;line-height:43px">Ready to<br>move<br>forward?</h2>
  <div class="badge" style="left:20px;top:195px">
    <svg width="9" height="10" viewBox="0 0 9 10"><path d="M4.5 .5 8.5 2v3c0 2.5-2 4-4 4.5C2.5 9 .5 7.5.5 5V2z" fill="none" stroke="#22edc1" stroke-width=".8"/><path d="M2.8 5l1.2 1.2 2.2-2.4" fill="none" stroke="#22edc1" stroke-width=".8"/></svg>
    <span>Having a hard time looking<br>for a merchant account?</span></div>
  <div class="badge" style="left:136px;top:195px">
    <svg width="9" height="10" viewBox="0 0 9 10"><path d="M4.5 .5 8.5 2v3c0 2.5-2 4-4 4.5C2.5 9 .5 7.5.5 5V2z" fill="none" stroke="#22edc1" stroke-width=".8"/><path d="M2.8 5l1.2 1.2 2.2-2.4" fill="none" stroke="#22edc1" stroke-width=".8"/></svg>
    <span>Having a hard time looking<br>for a merchant account?</span></div>
  <div class="phone" role="img" aria-label="Smartphone showing the app screen" style="left:278px;top:46px;width:122px;height:230px;border-radius:20px"></div>
  <div class="side-dots"><i></i><i></i><i></i></div>
</section>

<!-- ROW 3 -->
<section class="screen dark" style="left:80px;top:662px">
  <div class="art" role="img" aria-label="Mint line drawing of large sweeping curves" style="left:0;top:20px;width:190px;height:237px;background:radial-gradient(ellipse at 40% 50%,rgba(34,237,193,.18),transparent 70%)"></div>
  <nav class="nav"><div class="nav-links"><span>Home</span><span>Industries</span><span>Solutions</span><span>Blog</span><span>Contact</span></div><div class="brand">BROVA</div><span class="login">Log in</span></nav>
  <h2 class="section-title caps" style="left:196px;top:72px;font-size:42px">HIGH RISK</h2>
  <p style="position:absolute;left:197px;top:143px;font-size:7px"><span class="green">Pay</span> Interchange costs <span class="green">+ 2%</span></p>
  <p class="para" style="left:334px;top:142px">Applying and getting approved for a merchant account isn't always simple, especially for businesses seen as high-risk.</p>
  <div class="rule" style="left:197px;top:180px;width:240px"></div>
  <span class="btn" style="position:absolute;left:196px;top:204px">Get Started</span>
  <div class="side-dots"><i></i><i></i><i></i></div>
</section>

<section class="screen dark" style="left:572px;top:662px">
  <div class="art" role="img" aria-label="Mint line drawing of large sweeping curves" style="left:280px;top:0;width:178px;height:257px;background:radial-gradient(ellipse at 60% 50%,rgba(34,237,193,.18),transparent 70%)"></div>
  <nav class="nav"><div class="nav-links"><span>Home</span><span>Industries</span><span>Solutions</span><span>Blog</span><span>Contact</span></div><div class="brand">BROVA</div><span class="login">Log in</span></nav>
  <h2 class="section-title caps" style="left:20px;top:72px;font-size:42px">HIGH RISK</h2>
  <p style="position:absolute;left:20px;top:143px;font-size:7px"><span class="green">Pay</span> Interchange costs <span class="green">+ 2%</span></p>
  <p class="para" style="left:156px;top:142px">Applying and getting approved for a merchant account isn't always simple, especially for businesses seen as high-risk.</p>
  <div class="rule" style="left:20px;top:180px;width:240px"></div>
  <span class="btn" style="position:absolute;left:30px;top:204px">Get Started</span>
  <div class="side-dots"><i></i><i></i><i></i></div>
</section>

<section class="screen light" style="left:1065px;top:662px">
  <nav class="nav"><div class="nav-links"><span>Home</span><span>Industries</span><span>Solutions</span><span>Blog</span><span>Contact</span></div><div class="brand">BROVA</div><span class="login">Log in</span></nav>
  <h2 class="section-title" style="left:20px;top:77px;font-size:26px;color:var(--deep)">HIGH RISK</h2>
  <div class="arrow-dot" style="left:338px;top:78px"><svg width="6" height="8" viewBox="0 0 6 8"><path d="M3 0v7M.5 4.5 3 7l2.5-2.5" fill="none" stroke="#fff" stroke-width=".8"/></svg></div>
  <div class="rule" style="left:20px;top:117px;width:348px"></div>
  <h2 class="section-title" style="left:20px;top:139px;font-size:26px;color:var(--deep)">CONVENIENCE FEES</h2>
  <div class="arrow-dot" style="left:338px;top:141px"><svg width="6" height="8" viewBox="0 0 6 8"><path d="M3 0v7M.5 4.5 3 7l2.5-2.5" fill="none" stroke="#fff" stroke-width=".8"/></svg></div>
  <div class="rule" style="left:20px;top:180px;width:348px"></div>
  <span class="btn" style="position:absolute;left:328px;top:212px">Get Started</span>
  <div class="side-dots"><i></i><i></i><i></i></div>
</section>

<section class="screen light" style="left:1558px;top:662px">
  <div class="art" role="img" aria-label="Thin black line drawing of large sweeping curves" style="left:290px;top:0;width:168px;height:257px;background:radial-gradient(ellipse at 60% 50%,rgba(0,0,0,.07),transparent 70%)"></div>
  <nav class="nav"><div class="nav-links"><span>Home</span><span>Industries</span><span>Solutions</span><span>Blog</span><span>Contact</span></div><div class="brand">BROVA</div><span class="login">Log in</span></nav>
  <h2 class="section-title caps" style="left:20px;top:72px;font-size:42px;color:var(--deep)">HIGH RISK</h2>
  <p style="position:absolute;left:20px;top:143px;font-size:7px">Pay Interchange costs + 2%</p>
  <p class="para" style="left:156px;top:142px">Applying and getting approved for a merchant account isn't always simple, especially for businesses seen as high-risk.</p>
  <div class="rule" style="left:20px;top:180px;width:240px"></div>
  <span class="btn" style="position:absolute;left:30px;top:204px">Get Started</span>
  <div class="side-dots"><i></i><i></i><i></i></div>
</section>

<section class="screen dark-teal" style="left:2051px;top:662px;background:linear-gradient(200deg,#1c1f1f 20%,#2a5349 100%)">
  <nav class="nav"><div class="nav-links"><span>Home</span><span>Industries</span><span>Solutions</span><span>Blog</span><span>Contact</span></div><div class="brand">BROVA</div><span class="login">Log in</span></nav>
  <p style="position:absolute;left:61px;top:94px;font-size:4px" class="green">High Risk</p>
  <p style="position:absolute;left:61px;top:106px;width:340px;font-size:10px;line-height:13px">Lorem Ipsum! Applying and getting approved for a merchant payment account isn't always a simple matter, especially for businesses that are considered “high-risk” by financial institutions or payment processors.</p>
  <span class="btn" style="position:absolute;left:58px;top:202px">Get Started</span>
  <div class="side-dots"><i></i><i></i><i></i></div>
</section>

<!-- ROW 4 -->
<section class="screen light" style="left:80px;top:955px;background:var(--paper-2)">
  <nav class="nav"><div class="nav-links"><span>Home</span><span>Industries</span><span>Solutions</span><span>Blog</span><span>Contact</span></div><div class="brand">BROVA</div><span class="login" style="background:none;border:.5px solid rgba(0,0,0,.3)">Log in</span></nav>
  <h2 class="section-title caps" style="left:19px;top:36px;font-size:71px;line-height:74px;color:var(--deep)">CONVENIE-<br>NCE FEES</h2>
  <p style="position:absolute;left:19px;top:209px;font-size:7px;line-height:8px;color:var(--deep)">Pass your fees<br><span style="color:var(--muted)">to your customers</span></p>
  <p class="para" style="left:126px;top:208px">Applying and getting approved for a merchant account isn't always simple, especially for businesses seen as high-risk.</p>
  <span class="btn" style="position:absolute;left:362px;top:212px">Get Started</span>
  <div class="side-dots"><i></i><i></i><i></i></div>
</section>

<section class="screen dark" style="left:572px;top:955px;background:linear-gradient(170deg,#1c3a33 0%,var(--ink) 40%,#1f2523 70%,var(--deep) 130%)">
  <nav class="nav"><div class="nav-links"><span>Home</span><span>Industries</span><span>Solutions</span><span>Blog</span><span>Contact</span></div><div class="brand">BROVA</div><span class="login">Log in</span></nav>
  <h2 class="section-title caps" style="left:19px;top:36px;font-size:71px;line-height:74px">CONVENIE-<br>NCE FEES</h2>
  <p style="position:absolute;left:19px;top:209px;font-size:7px;line-height:8px"><span class="green">Pass your fees</span><br>to your customers</p>
  <p class="para" style="left:126px;top:208px">Applying and getting approved for a merchant account isn't always simple, especially for businesses seen as high-risk.</p>
  <span class="btn" style="position:absolute;left:362px;top:212px">Get Started</span>
  <div class="side-dots"><i></i><i></i><i></i></div>
</section>

<section class="screen screen--short light" style="left:1065px;top:955px">
  <nav class="nav"><div class="nav-links"><span>Home</span><span>Industries</span><span>Solutions</span><span>Blog</span><span>Contact</span></div><div class="brand">BROVA</div><span class="login">Log in</span></nav>
  <h2 class="section-title" style="left:20px;top:34px;font-size:18px;line-height:21px;font-weight:600">Processing over<br>50.000$ montly?</h2>
  <p style="position:absolute;left:20px;top:82px;font-size:7px">Contact us for a custom quote</p>
  <p style="position:absolute;left:20px;top:94px;font-size:3px;color:var(--muted)">Let us help you</p>
  <span class="btn" style="position:absolute;left:18px;top:133px">Get Started</span>
  <div class="art" role="img" aria-label="Black line wireframe globe" style="left:240px;top:0;width:180px;height:173px;border-radius:50%;background:radial-gradient(circle,rgba(0,0,0,.08),transparent 70%)"></div>
  <div class="side-dots" style="bottom:12px"><i></i><i></i><i></i></div>
</section>

<section class="screen screen--short dark" style="left:1558px;top:955px">
  <nav class="nav"><div class="nav-links"><span>Home</span><span>Industries</span><span>Solutions</span><span>Blog</span><span>Contact</span></div><div class="brand">BROVA</div><span class="login">Log in</span></nav>
  <h2 class="section-title green" style="left:20px;top:34px;font-size:18px;line-height:21px;font-weight:600">Processing over<br>50.000$ montly?</h2>
  <p style="position:absolute;left:20px;top:82px;font-size:7px">Contact us for a custom quote</p>
  <p style="position:absolute;left:20px;top:94px;font-size:3px;color:var(--muted)">Let us help you</p>
  <span class="btn" style="position:absolute;left:18px;top:133px">Get Started</span>
  <div class="art" role="img" aria-label="Mint wireframe globe" style="left:240px;top:0;width:180px;height:173px;border-radius:50%;background:radial-gradient(circle,rgba(34,237,193,.25),transparent 70%)"></div>
</section>

</main>
</body>
</html>
```